Website for Kitchen Showroom

We need a website for our Kitchen Showroom. Will be 10 pages in total. Example of a website we like can be found at http://www.velmarabo.co.uk/ with the image on the front page being a java script slideshow picking up images from a directory that I can update. Looking for simple SEO
I have the wording/ sitemap/ images all ready to go and I am looking for a quick turn around.
Thank you for your time. Rob

```html
<!DOCTYPE html>
<html lang="en">
<head>
<meta charset="utf-8">
<title>Hearthline Kitchens</title>
<link rel="stylesheet" href="https://fonts.googleapis.com/css2?family=Titillium+Web:wght@300;400;700&display=swap">
<style>
  :root {
    --lime: #ccd629;
    --lime-dark: #9aa81e;
    --ink: #000000;
    --paper: #ffffff;
    --slate: #4d4d4d;
    --menu: #1a1614;
    --dots: #6f6f6f;
    --text-light: #e9e9e9;
  }
  * { box-sizing: border-box; margin: 0; padding: 0; }
  html, body {
    width: 1200px; height: 1200px; overflow: hidden;
    background: var(--ink);
    font-family: "Titillium Web", Arial, sans-serif;
  }
  .page { position: relative; width: 1200px; height: 1200px; }

  .hero {
    position: absolute; left: 0; top: 0; width: 1200px; height: 494px;
    background:
      linear-gradient(100deg, rgba(235,232,225,0.9) 0%, rgba(190,180,170,0.5) 30%, rgba(0,0,0,0) 55%),
      linear-gradient(180deg, #5a3a2c 0%, #7a3f2a 45%, #5b2a1e 70%, #b98f6a 100%);
  }

  .headline { position: absolute; left: 53px; font-weight: 700; line-height: 1; }
  .headline--top {
    top: 63px; width: 630px; height: 75px; background: var(--paper);
    color: var(--ink); font-size: 66px; padding: 4px 0 0 113px;
  }
  .headline--bottom {
    top: 154px; width: 541px; height: 75px; background: var(--lime);
    color: var(--paper); font-size: 66px; padding: 4px 0 0 113px;
  }
  .headline-chevron { position: absolute; left: 50px; top: 70px; z-index: 2; }

  .brand {
    position: absolute; left: 49px; top: 379px; width: 351px; height: 135px;
    background: var(--paper);
    display: flex; align-items: center; gap: 14px; padding-left: 26px;
  }
  .brand-square { width: 40px; height: 40px; background: var(--lime-dark); flex: none; }
  .brand-name { color: #8a8a8a; font-weight: 300; font-size: 36px; line-height: 1; }

  .brand-rule {
    position: absolute; left: 49px; top: 528px; width: 351px; height: 16px;
    background: repeating-linear-gradient(90deg, var(--dots) 0 2px, transparent 2px 3px);
  }

  .submenu {
    position: absolute; left: 418px; top: 326px; width: 154px; height: 170px;
    background: var(--menu); list-style: none; padding: 6px 10px 0 10px;
  }
  .submenu li {
    color: var(--paper); font-size: 19px; line-height: 1.05;
    padding: 3px 0 7px; border-bottom: 2px dotted var(--lime);
    margin-bottom: 6px;
  }
  .submenu li:last-child { margin-bottom: 0; }

  .main-nav { position: absolute; left: 0; top: 522px; width: 1200px; height: 32px; }
  .nav-mark {
    position: absolute; top: 5px; width: 23px; height: 23px;
    background: repeating-linear-gradient(0deg, var(--lime) 0 2px, #4f5a10 2px 3px);
  }
  .nav-item {
    position: absolute; top: 0; color: var(--paper);
    font-size: 20px; line-height: 32px; font-weight: 400;
  }

  .intro-title {
    position: absolute; left: 49px; top: 655px; color: var(--paper);
    font-size: 20px; line-height: 1; font-weight: 400;
  }
  .intro-rule {
    position: absolute; left: 49px; top: 696px; width: 1099px;
    border-top: 2px dotted var(--dots);
  }

  .content {
    position: absolute; left: 0; top: 715px; width: 1200px; height: 371px;
    background: var(--slate);
  }
  .content-cols {
    position: absolute; left: 49px; top: 71px; width: 1099px; height: 242px;
    columns: 2; column-gap: 33px; column-fill: auto;
    color: var(--text-light); font-weight: 300; font-size: 16.5px; line-height: 22px;
    hyphens: auto;
  }
  .content-cols p { margin-bottom: 22px; }

  .footer-note {
    position: absolute; right: 49px; top: 1160px;
    color: #9a9a9a; font-size: 13px; font-weight: 300;
  }
</style>
</head>
<body>
<div class="page">
  <div class="hero" role="img" aria-label="Photograph of a modern kitchen with polished timber cabinets, a granite island bench and stainless steel appliances"></div>

  <div class="headline headline--top">POP INTO OUR</div>
  <div class="headline headline--bottom">SHOWROOM.</div>
  <svg class="headline-chevron" width="56" height="62" viewBox="0 0 56 62" aria-hidden="true">
    <polygon points="0,0 22,0 50,31 22,62 0,62 28,31" fill="#ccd629"/>
  </svg>

  <ul class="submenu">
    <li>INSTALLATION</li>
    <li>ORDER</li>
    <li>KITCHEN DESIGNERS</li>
    <li>CONSULTATION</li>
  </ul>

  <div class="brand">
    <span class="brand-square"></span>
    <span class="brand-name">hearthline kitchens</span>
  </div>
  <div class="brand-rule"></div>

  <nav class="main-nav">
    <span class="nav-mark" style="left:424px"></span><span class="nav-item" style="left:475px">DESIGN</span>
    <span class="nav-mark" style="left:568px"></span><span class="nav-item" style="left:619px">GALLERY</span>
    <span class="nav-mark" style="left:732px"></span><span class="nav-item" style="left:783px">QUALITY</span>
    <span class="nav-mark" style="left:875px"></span><span class="nav-item" style="left:925px">LINKS</span>
    <span class="nav-mark" style="left:1003px"></span><span class="nav-item" style="left:1051px">CONTACT</span>
  </nav>

  <h1 class="intro-title">Designer Kitchens by Hearthline Kitchens</h1>
  <div class="intro-rule"></div>

  <section class="content">
    <div class="content-cols">
      <p>Welcome to Hearthline Kitchens, the region’s exclusive kitchen manufacturer based in Marrowdale. If you are seeking the highest quality kitchen, yet at a price that is a little more affordable, Hearthline Kitchens is the company you’ve been searching for.</p>
      <p>Hearthline Kitchens showroom is located less than 20 kilometers from the city centre, so easy to get to with easy access from Harbour Road.</p>
      <p>On this site, you can view some of our designer kitchens, read testimonials from our clients or just browse through our site to find out more. We hope you will find our site inspiring and put Hearthline Kitchens at the top of your list of kitchen showrooms you simply must visit.</p>
      <p>Pop into our showroom. We can chat about your plans and ideas for your new kitchen and maybe we can give you a few ideas of our own. Or contact us to arrange a no obligation consultation with one of our kitchen designers and if required we will bring the showroom to you.</p>
    </div>
  </section>

  <footer class="footer-note">© Hearthline Kitchens 2011</footer>
</div>
</body>
</html>
```